Premium men's gut health supplement needs a bottle label designed

We’re velnora - a premium men’s wellness brand focused on gut health. Our first product is a high-quality daily supplement designed to support digestion, regularity, and internal cleanliness. Backed by science and tailored for modern lifestyles, velnora is crafted in the UK and proudly LGBT-owned. It aims to resolve intimacy problems that gay men may experience due to poor digestion but also does not exclude any other orientation - other men may use it simply to improve their digestion.

velnora is for health-conscious men who value science-backed supplements and want to feel confident from the inside out. Many of our early adopters will be gay and bisexual men who prioritise gut health as part of their self-care, sexual, and hygiene routine, though the product is equally effective and appealing to anyone seeking premium digestive support.

The product is premium the target customer is male, not specific to one location but primary markets will be US, UK and EU.

I’d like a supplement bottle designed for velnora, our premium men’s gut health brand. The focus should be clean, slightly clinical, and minimal - inspired by brands like Quelrin and Darvo. The key element is the wordmark (velnora) on the front, with no additional logo or icon. Lowercase text and a strong, contemporary font are preferred.

The bottle should be aesthetically pleasing so that people are proud to display it on their shelf, instead of hiding it in a cupboard (like Quelrin, darvo, Pia Venturek, Morvanel etc)

Avoid anything that shows the product as being for LGBT, e.g., no rainbows, men holding hands etc.

The design should be premium, minimalist and not be busy or overwhelming.

I have uploaded a file called "Bottle" to give an idea of the type of container, but please ignore the colours and change as you see fit. This is just for reference for the type of bottle we'll use - all colours are customisable.

I have also uploaded some images for "style" reference, e.g., darvo, quelrin, pia venturek, etc for inspiration.

```html
<!DOCTYPE html>
<html lang="en">
<head>
<meta charset="utf-8">
<title>velnora – Health Supplements For Man</title>
<link rel="stylesheet" href="https://fonts.googleapis.com/css2?family=Josefin+Sans:wght@300;400;600&display=swap">
<style>
  :root {
    --backdrop: #7f7f7f;
    --label-dark: #1d1a1b;
    --label-mid: #2c292a;
    --gold: #c6a46a;
    --gold-light: #dcc08a;
    --gold-deep: #9c7c45;
    --ink-light: #ece8e0;
    --ink-dark: #1b1819;
  }
  * { margin: 0; padding: 0; box-sizing: border-box; }
  html, body {
    width: 1200px;
    height: 829px;
    overflow: hidden;
    background: var(--backdrop);
    font-family: "Josefin Sans", sans-serif;
  }
  .canvas {
    position: relative;
    width: 1200px;
    height: 829px;
  }
  .label {
    position: absolute;
    left: 276px;
    top: 44px;
    width: 648px;
    height: 740px;
    background: linear-gradient(180deg, var(--label-dark) 0%, var(--label-mid) 45%, var(--label-dark) 100%);
  }
  .gold-band {
    position: absolute;
    left: 0;
    width: 100%;
    height: 12px;
    background: linear-gradient(90deg, var(--gold-deep), var(--gold-light) 50%, var(--gold-deep));
  }
  .gold-band--top { top: 0; }
  .gold-band--bottom { bottom: 10px; }
  .wordmark {
    position: absolute;
    top: 120px;
    left: 0;
    width: 100%;
    text-align: center;
    font-weight: 300;
    font-size: 140px;
    line-height: 1;
    letter-spacing: 2px;
    color: var(--gold);
  }
  .descriptor {
    position: absolute;
    left: 0;
    width: 100%;
    text-align: center;
    font-weight: 300;
    font-size: 26px;
    letter-spacing: 3px;
  }
  .descriptor--category { top: 598px; color: var(--ink-light); }
  .descriptor--audience { top: 638px; color: var(--gold); }
  .count-tab {
    position: absolute;
    left: 199px;
    top: 672px;
    width: 250px;
    height: 58px;
  }
  .count-tab svg { position: absolute; inset: 0; }
  .count-tab__text {
    position: absolute;
    inset: 0;
    display: flex;
    align-items: center;
    justify-content: center;
    padding-top: 4px;
    font-weight: 600;
    font-size: 27px;
    letter-spacing: 1.5px;
    color: var(--ink-light);
  }
</style>
</head>
<body>
  <main class="canvas">
    <section class="label">
      <div class="gold-band gold-band--top"></div>
      <h1 class="wordmark">velnora</h1>
      <p class="descriptor descriptor--category">Health Supplements</p>
      <p class="descriptor descriptor--audience">For Man</p>
      <div class="count-tab">
        <svg viewBox="0 0 250 58" width="250" height="58" aria-hidden="true">
          <defs>
            <linearGradient id="tabGold" x1="0" y1="0" x2="0" y2="1">
              <stop offset="0" stop-color="#dcc08a"/>
              <stop offset="1" stop-color="#a9874e"/>
            </linearGradient>
          </defs>
          <path d="M0 58 C14 58 12 48 14 30 C16 10 18 4 32 4 L218 4 C232 4 234 10 236 30 C238 48 236 58 250 58 Z" fill="url(#tabGold)"/>
        </svg>
        <span class="count-tab__text">30 Capsules</span>
      </div>
      <div class="gold-band gold-band--bottom"></div>
    </section>
  </main>
</body>
</html>
```